Business Card: RW Office Partners - Your tidy answer finder

Business Name: RW Office Partners
Website: www.rwofficepartners.com.au
Email: marisol@rwofficepartners.com.au
Mobile: 61 487 902 346
Facebook: @rwofficepartners
Instrgram: @rwofficepartners

Brading Colours:
HEX
#986474
#ddccd3
#7a8498
#c9d8e4
#000000
#ffffff

Tag Line: Your organised problem solver

Link to DRAFT website:
https://helpdeskhub.sitebuilderx.com/rw-office-partners

About Page from the website:
My name is Marisol Bramwell, and I would love to assist you to become more productive in your day to day and achieve your business and personal goals.
My mission is to give you time, time to work on the important tasks of your business or to be able to spend more time with your family. I will take on the tasks you don’t have time for, don’t know well or simply don’t like to do.
I have an extensive background in Administration, Tender Coordination, Document Control, WHS and Quality Management working primarily in the Construction, Mining and Corporate World.
I am passionate about being organised, having order and making things in your life (and mine) easier! I love to watch something unfold and grow into something amazing! I am known for being the go-to problem solver, the organiser of all things, producing high standards of work even under pressure. I’m also a confident communicator, and I understand that you’re busy running your business.

Target Market(s)

Small to Medium Business who require assistance in their business by a virtual assistant.

Industry/Entity Type

Virtual Assistant

Contact Information for Business Card

Mobile: 61 487 902 346

Font styles to use
Sans Serif

Colors
ffffff

Requirements
Must have
• Branding Colours as outlined.
Contact Details as outlined.
Logo as provided.
Proper contact details - mobile, facebook, instragm, website.
Simple, Elegant, very clean looking.
Should not have
• Note cute with pictures.
Not too girly as still want to market to construction companies.

```html
<!DOCTYPE html>
<html lang="en">
<head>
<meta charset="utf-8">
<title>RW Office Partners – Business Card</title>
<link rel="stylesheet" href="https://fonts.googleapis.com/css2?family=Montserrat:wght@400;500;700;800&display=swap">
<style>
  :root {
    --mauve: #986474;
    --blush: #ddccd3;
    --slate: #7a8498;
    --mist: #c9d8e4;
    --ink: #000000;
    --paper: #ffffff;
    --stripe-soft: #eef1f6;
    --card-shadow: rgba(0, 0, 0, 0.13);
  }
  * { box-sizing: border-box; margin: 0; padding: 0; }
  html, body {
    width: 1015px;
    height: 1200px;
    overflow: hidden;
    background: var(--paper);
    font-family: "Montserrat", Arial, sans-serif;
    color: var(--ink);
  }
  .canvas { position: relative; width: 1015px; height: 1200px; }

  .card {
    position: absolute;
    background: var(--paper);
    box-shadow: 16px 16px 14px var(--card-shadow);
    overflow: hidden;
  }

  /* Front */
  .card--front { left: 32px; top: 22px; width: 933px; height: 548px; }
  .front-texture {
    position: absolute;
    left: 0; top: 0;
    width: 270px; height: 548px;
    background: linear-gradient(135deg, var(--stripe-soft) 0%, rgba(238,241,246,0.5) 60%, rgba(238,241,246,0) 100%);
    clip-path: polygon(0 0, 270px 0, 0 270px, 0 330px, 270px 548px, 0 548px);
  }
  .brand {
    position: absolute;
    left: 0; right: 0; top: 200px;
    display: flex;
    justify-content: center;
    align-items: center;
    gap: 26px;
  }
  .brand-mark {
    width: 108px; height: 108px;
    background: var(--mauve);
  }
  .brand-name {
    font-weight: 500;
    font-size: 60px;
    line-height: 0.98;
    letter-spacing: 1px;
    color: var(--slate);
    text-transform: uppercase;
  }
  .tagline {
    position: absolute;
    left: 0; right: 0; top: 367px;
    text-align: center;
    font-size: 14px;
    font-weight: 500;
    letter-spacing: 6.2px;
    text-transform: uppercase;
  }

  /* Back */
  .card--back { left: 50px; top: 620px; width: 915px; height: 533px; }
  .back-band {
    position: absolute;
    left: 37px; bottom: 0;
    width: 824px; height: 16px;
    background: var(--mist);
  }
  .holder {
    position: absolute;
    right: 571px; top: 187px;
    text-align: right;
  }
  .holder-name {
    font-weight: 800;
    font-size: 50px;
    line-height: 1.05;
    letter-spacing: 3px;
    text-transform: uppercase;
  }
  .holder-company {
    margin-top: 26px;
    font-size: 17px;
    letter-spacing: 1.4px;
    text-transform: uppercase;
  }
  .divider {
    position: absolute;
    left: 394px; top: 208px;
    width: 2px; height: 121px;
    background: var(--slate);
  }
  .contact-list {
    position: absolute;
    left: 443px; top: 172px;
    list-style: none;
  }
  .contact-item {
    display: flex;
    align-items: center;
    height: 41.3px;
    font-size: 15px;
    letter-spacing: 1.3px;
    text-transform: uppercase;
  }
  .contact-icon {
    width: 26px; height: 26px;
    margin-right: 16px;
    flex: none;
  }
</style>
</head>
<body>
<main class="canvas">

  <section class="card card--front" aria-label="Card front">
    <div class="front-texture" role="img" aria-label="Soft diagonal stripe texture in pale grey-blue"></div>
    <div class="brand">
      <span class="brand-mark" aria-hidden="true"></span>
      <p class="brand-name">RW Office<br>Partners</p>
    </div>
    <p class="tagline">Your tidy answer finder</p>
  </section>

  <section class="card card--back" aria-label="Card back">
    <div class="holder">
      <h1 class="holder-name">Marisol<br>Bramwell</h1>
      <p class="holder-company">RW Office Partners</p>
    </div>
    <span class="divider" aria-hidden="true"></span>

    <ul class="contact-list">
      <li class="contact-item">
        <svg class="contact-icon" viewBox="0 0 26 26" aria-hidden="true">
          <circle cx="13" cy="13" r="13" fill="var(--mauve)"/>
          <path d="M7 13.2 13 7.8l6 5.4h-1.8v5.3h-3v-3.4h-2.4v3.4h-3v-5.3z" fill="#fff"/>
        </svg>
        www.rwofficepartners.com.au
      </li>
      <li class="contact-item">
        <svg class="contact-icon" viewBox="0 0 26 26" aria-hidden="true">
          <circle cx="13" cy="13" r="13" fill="var(--mauve)"/>
          <rect x="7.5" y="9" width="11" height="8" fill="none" stroke="#fff" stroke-width="1.3"/>
          <path d="M7.5 9 13 13.5 18.5 9" fill="none" stroke="#fff" stroke-width="1.3"/>
        </svg>
        marisol@rwofficepartners.com.au
      </li>
      <li class="contact-item">
        <svg class="contact-icon" viewBox="0 0 26 26" aria-hidden="true">
          <circle cx="13" cy="13" r="13" fill="var(--mauve)"/>
          <rect x="10" y="6.5" width="6.5" height="13" rx="1.2" fill="none" stroke="#fff" stroke-width="1.3" transform="rotate(20 13 13)"/>
        </svg>
        61 487 902 346
      </li>
      <li class="contact-item">
        <svg class="contact-icon" viewBox="0 0 26 26" aria-hidden="true">
          <circle cx="13" cy="13" r="13" fill="var(--mauve)"/>
        </svg>
        @rwofficepartners
      </li>
      <li class="contact-item">
        <svg class="contact-icon" viewBox="0 0 26 26" aria-hidden="true">
          <circle cx="13" cy="13" r="13" fill="var(--mauve)"/>
        </svg>
        @rwofficepartners
      </li>
    </ul>

    <span class="back-band" aria-hidden="true"></span>
  </section>

</main>
</body>
</html>
```